Global social media analytics company needs business card design

We need an updated business card design to align with our new website - brightquillo.net -

I would also like a favicon designed as well.

Target Market(s)

CEOs, CMOs go big companies

Industry/Entity Type

Business

Contact Information for Business Card

Room for the following:
Address
Main telephone
Direct telephone or cell phone
twitter handle

Colors
aaaaaa

Requirements
Must have
• Attention to detail; style.
• Use the logo color from our website - which is gray

```html
<!DOCTYPE html>
<html lang="en">
<head>
<meta charset="utf-8">
<title>Brightquillo Stationery</title>
<link href="https://fonts.googleapis.com/css2?family=Montserrat:wght@300;400;600&display=swap" rel="stylesheet">
<style>
  :root{
    --backdrop:#e6e6e6;
    --paper:#ffffff;
    --brand-gray:#8f8f8f;
    --text-gray:#6f6f6f;
    --rule-gray:#b5b5b5;
    --light-gray:#aaaaaa;
    --shadow:rgba(0,0,0,.12);
  }
  *{box-sizing:border-box;margin:0;padding:0}
  html,body{width:1200px;height:706px;overflow:hidden}
  body{background:var(--backdrop);font-family:"Montserrat",sans-serif;color:var(--text-gray);position:relative}

  .brand{display:flex;align-items:center;gap:6px}
  .brand-dot{border-radius:50%;background:var(--brand-gray);flex:none}
  .brand-name{font-weight:600;color:var(--brand-gray);letter-spacing:-.01em}

  /* Business cards */
  .card{position:absolute;width:290px;height:166px;background:var(--paper);box-shadow:0 2px 6px var(--shadow)}
  .card-back{left:110px;top:120px;padding:28px 26px}
  .card-back .brand-dot{width:26px;height:26px}
  .card-back .brand-name{font-size:20px}
  .card-back .card-rule{position:absolute;left:26px;right:26px;bottom:34px;border-top:1px solid var(--rule-gray)}
  .card-back .card-site{position:absolute;right:26px;bottom:20px;font-size:7px;letter-spacing:.05em}

  .card-front{left:110px;top:370px;padding:24px 26px}
  .card-front .brand-dot{width:26px;height:26px}
  .card-front .brand-name{font-size:20px}
  .card-name{margin-top:14px;font-size:9px;letter-spacing:.2em;text-transform:uppercase;color:var(--text-gray)}
  .card-name span{font-weight:300}
  .card-rule{border-top:1px solid var(--rule-gray);margin-top:16px}
  .card-contacts{display:flex;margin-top:8px;font-size:6.5px;line-height:1.6}
  .card-contacts .col{padding:0 8px;border-left:1px solid var(--rule-gray)}
  .card-contacts .col:first-child{padding-left:0;border-left:none}
  .ico-line{display:flex;align-items:center;gap:4px}
  .ico{width:7px;height:7px;border-radius:50%;background:var(--light-gray);flex:none}

  /* Letterhead */
  .letter{position:absolute;left:640px;top:28px;width:462px;height:650px;background:var(--paper);box-shadow:0 3px 8px var(--shadow);padding:40px 44px}
  .letter .brand-dot{width:34px;height:34px}
  .letter .brand-name{font-size:25px}
  .letter-head{margin:56px 0 0 56px;font-size:7px;line-height:1.5}
  .letter-body{margin:8px 0 0 56px;font-size:6.4px;line-height:1.55;text-align:justify}
  .letter-body p{margin-bottom:10px}
  .letter-body p:first-child{text-indent:10px}
  .signature{margin:6px 0 0 56px;width:110px;height:44px;border-radius:22px;background:linear-gradient(90deg,#d9dbe4,#eceef3)}
  .letter-foot{position:absolute;left:44px;right:44px;bottom:44px;border-top:1px solid var(--rule-gray);padding-top:12px;display:flex;font-size:8px;line-height:1.7;letter-spacing:.08em}
  .letter-foot .col{padding:0 16px;border-left:1px solid var(--rule-gray)}
  .letter-foot .col:first-child{padding-left:0;border-left:none}
  .letter-foot .ico{width:9px;height:9px}
</style>
</head>
<body>

<section class="card card-back" aria-label="Business card back">
  <div class="brand"><span class="brand-dot"></span><span class="brand-name">brightquillo</span></div>
  <div class="card-rule"></div>
  <div class="card-site">www.brightquillo.net</div>
</section>

<section class="card card-front" aria-label="Business card front">
  <div class="brand"><span class="brand-dot"></span><span class="brand-name">brightquillo</span></div>
  <div class="card-name">Daniel Marsh <span>· CEO</span></div>
  <div class="card-rule"></div>
  <div class="card-contacts">
    <div class="col">218 Harborview St. 3rd Fl<br>Easton, MA 02375 USA</div>
    <div class="col">
      <div class="ico-line"><span class="ico"></span>+1 555 310 4420</div>
      <div class="ico-line"><span class="ico"></span>+1 555 310 4400</div>
    </div>
    <div class="col">
      <div class="ico-line"><span class="ico"></span>@brightquillo</div>
      <div class="ico-line"><span class="ico"></span>brightquillo.net</div>
    </div>
  </div>
</section>

<section class="letter" aria-label="Letterhead">
  <div class="brand"><span class="brand-dot"></span><span class="brand-name">brightquillo</span></div>
  <div class="letter-head">Brightquillo<br>December 22, 2011/Revised February 2, 2013</div>
  <div class="letter-body">
    <p>Lorem ipsum dolor sit amet, consectetur adipiscing elit. Sed libero est, pellentesque facilisis tempor eu, pulvinar vitae justo. Praesent bibendum ultricies magna luctus luctus. Suspendisse potenti. Pellentesque habitant morbi tristique senectus et netus et malesuada fames ac turpis egestas. Nullam elit urna, porttitor quis luctus ac, gravida in ante. Vestibulum ante ipsum primis in faucibus orci luctus et ultrices posuere cubilia curae. Praesent auctor aliquet tempor. Curabitur vel leo quis eros dapibus rutrum. Pellentesque accumsan, diam vel tristique dictum, leo magna pellentesque justo, non ullamcorper sapien justo et dui. Nam et nulla.</p>
    <p>Donec consectetur tempor purus. Nullam turpis lacus, molestie bibendum auctor non, convallis quis mauris. Cum sociis natoque penatibus et magnis dis parturient montes, nascetur ridiculus mus. Aenean feugiat erat sit amet massa semper ullamcorper lobortis massa interdum. Fusce turpis nunc, pellentesque quis accumsan viverra, tempor vel sem. Etiam varius, velit et pretium cursus, lorem massa consequat orci, sit amet interdum turpis nibh ac eros. Nam et tellus nulla, eget congue nisl. Mauris vitae sapien ut quam malesuada suscipit mattis sed nulla. Ut dictum tellus vel metus eleifend tincidunt. Proin aliquet enim sit amet est faucibus nec molestie ligula dignissim. Nam tempor ligula non nunc eleifend tempor. Maecenas fermentum nunc vel diam ultrices vulputate sed vitae elit. Nam vitae dui tortor, quis scelerisque velit. Sed pretium blandit odio, vel malesuada purus convallis.</p>
    <p>Donec consectetur tempor purus. Nullam turpis lacus, molestie bibendum auctor non, convallis quis mauris. Cum sociis natoque penatibus et magnis dis parturient montes, nascetur ridiculus mus. Aenean feugiat erat sit amet massa semper ullamcorper lobortis massa interdum. Fusce turpis nunc, pellentesque quis accumsan viverra, tempor vel sem. Etiam varius, velit et pretium cursus, lorem massa consequat orci, sit amet interdum turpis nibh ac eros. Nam et tellus nulla, eget congue nisl. Mauris dui tortor, quis scelerisque velit. Sed pretium blandit odio, vel malesuada purus convallis vitae. Aliquam erat volutpat.</p>
    <p>Donec consectetur tempor purus. Nullam turpis lacus, molestie bibendum auctor non, convallis quis mauris. Cum sociis natoque penatibus et magnis dis parturient montes, nascetur ridiculus mus. Aenean feugiat erat sit amet massa semper ullamcorper lobortis massa interdum. Fusce turpis nunc, pellentesque quis accumsan viverra, tempor vel sem. Etiam varius, velit et pretium cursus, lorem massa consequat orci, sit amet interdum turpis nibh ac eros. Nam et tellus nulla, eget congue nisl. Mauris vitae sapien ut quam malesuada suscipit mattis sed nulla. Ut dictum tellus vel metus eleifend tincidunt. Proin aliquet enim sit amet est faucibus nec molestie ligula dignissim. Nam tempor ligula non nunc eleifend tempor. Sed pretium blandit odio, vel malesuada purus convallis vitae.</p>
  </div>
  <div class="signature" role="img" aria-label="Handwritten signature with approval stamp"></div>
  <div class="letter-foot">
    <div class="col">218 Harborview St. 3rd Fl<br>Easton, MA 02375 USA</div>
    <div class="col">
      <div class="ico-line"><span class="ico"></span>+1 555 310 4420</div>
      <div class="ico-line"><span class="ico"></span>+1 555 310 4400</div>
    </div>
    <div class="col">
      <div class="ico-line"><span class="ico"></span>@brightquillo</div>
      <div class="ico-line"><span class="ico"></span>brightquillo.net</div>
    </div>
  </div>
</section>

</body>
</html>
```